Business Card Design Project

We need a business card for our new business based in Vancouver called
"Lumora Calm Haven" We are looking for a simple yet bold design for our business cards that will enable us to stand out from the pack. All business card details will be provided in the handover stage.
Updates

Thank you to all who have submitted

The work is great for the most part
Cards with creative use of the logo
have been more successful so far

Dark cards and rounded edges 
are also getting good reviews

Double sided is an option we would like to see explored

Thank you

Target Market(s)

Our clients are stressed business people, yoga/meditation enthusiast, and people looking for a new experience in a Spa enviroment

Industry/Entity Type

Business

Font styles to use
Other font styles liked:
• please check design file

Requirements
Must have
• Lumora Calm Haven

5218 E Kestrel Row, Vancouver, BC V5N 4K7

lumora@calmhaven.ca
Nice to have
• Creative approach to layout and design

Outside of the box design elements
Should not have
• Should not be too busy

```html
<!DOCTYPE html>
<html lang="en">
<head>
<meta charset="utf-8">
<title>Lumora Calm Haven — Business Card</title>
<link rel="stylesheet" href="https://fonts.googleapis.com/css2?family=Tinos&display=swap">
<style>
  :root {
    --ink: #4b4f92;
    --lavender-deep: #d3d2e4;
    --lavender-mid: #e6e5f0;
    --glow: #ffffff;
    --emblem: #b9bddb;
  }
  html, body {
    margin: 0;
    padding: 0;
    width: 1200px;
    height: 686px;
    overflow: hidden;
    background: var(--lavender-deep);
  }
  .card {
    position: relative;
    width: 1200px;
    height: 686px;
    overflow: hidden;
  }
  .card-art {
    position: absolute;
    inset: 0;
    display: block;
  }
  .brand-name {
    font-family: "Tinos", "Times New Roman", serif;
    font-size: 70px;
    fill: var(--ink);
    letter-spacing: 3px;
  }
  .brand-rule {
    stroke: var(--ink);
    stroke-width: 2;
  }
  .contact-line {
    font-family: "Tinos", "Times New Roman", serif;
    fill: var(--ink);
  }
  .contact-street { font-size: 78px; }
  .contact-city   { font-size: 80px; }
  .contact-email  { font-size: 72px; }
</style>
</head>
<body>
  <main class="card">
    <svg class="card-art" width="1200" height="686" viewBox="0 0 1200 686" xmlns="http://www.w3.org/2000/svg">
      <defs>
        <radialGradient id="centre-glow" cx="50%" cy="42%" r="60%">
          <stop offset="0" stop-color="var(--glow)"/>
          <stop offset="0.6" stop-color="#f4f3f9"/>
          <stop offset="1" stop-color="var(--lavender-mid)"/>
        </radialGradient>
        <radialGradient id="emblem-wash" cx="50%" cy="55%" r="50%">
          <stop offset="0" stop-color="var(--emblem)" stop-opacity="0.35"/>
          <stop offset="0.7" stop-color="var(--emblem)" stop-opacity="0.18"/>
          <stop offset="1" stop-color="var(--emblem)" stop-opacity="0"/>
        </radialGradient>
        <path id="street-path" d="M 263 474 Q 603 406 943 474"/>
        <path id="city-path"   d="M 149 586 Q 600 466 1051 586"/>
        <path id="email-path"  d="M 269 663 Q 591 627 914 663"/>
      </defs>

      <!-- background with a soft lens of light -->
      <rect class="bg-base" width="1200" height="686" fill="var(--lavender-deep)"/>
      <path class="bg-lens" d="M 0 40 Q 600 520 1200 40 L 1200 646 Q 600 160 0 646 Z" fill="url(#centre-glow)"/>
      <ellipse class="bg-halo" cx="600" cy="330" rx="520" ry="300" fill="url(#centre-glow)" opacity="0.8"/>

      <!-- emblem area -->
      <ellipse class="emblem-area" role="img" aria-label="Faint emblem of water drops falling into concentric ripples"
               cx="600" cy="380" rx="400" ry="310" fill="url(#emblem-wash)"/>

      <!-- brand name with plain rules -->
      <text class="brand-name" x="600" y="140" text-anchor="middle" textLength="560" lengthAdjust="spacing">Lumora Calm Haven</text>
      <line class="brand-rule" x1="303" y1="196" x2="851" y2="196"/>

      <!-- contact details -->
      <text class="contact-line contact-street" text-anchor="middle">
        <textPath href="#street-path" startOffset="50%">5218 E Kestrel Row</textPath>
      </text>
      <text class="contact-line contact-city" text-anchor="middle">
        <textPath href="#city-path" startOffset="50%">Vancouver, BC V5N 4K7</textPath>
      </text>
      <text class="contact-line contact-email" text-anchor="middle">
        <textPath href="#email-path" startOffset="50%">lumora@calmhaven.ca</textPath>
      </text>
    </svg>
  </main>
</body>
</html>
```